Egle Marcinkute - Armonici CD

We need a design for the CD cover.  Front and Back.  This is a classical music - soprano + orchestra cd release.  Needs to be a creative/traditional design.  we attach several photos of the artists for you to choose from. please feel free to use any graphics from www.thearmonici-example.org, or www.wbfenwickopera-example.org
Please see the records.thearmonici-example.org for the past submissions/projects.

Target Market(s)
Classical music lovers, mature audiences
Requirements
Must have
- Egle Marcinkute, soprano
Hartwell Armonici Chamber Orchestra
Tomas Brekvold, conductor
Logo of the Opera (FWO) (attached)
Logo of the Orchestra (attached)
Logo of the label (attached)
lists of tracks:
1 Vola, vola mia stella! from I fuochi di Serrano, Callari
2 Lume Serena from Gandolfo, Callari
3 Cantai d'Amore from Lidia, Rambetti
4 Una sera torneremo - Signora Gelsomina, Rambetti
5 Io son chiamata Lulù - La Pèlerine, Rambetti
6 Pura Stella from Tessaria, Tordassi
7 Ortensia's Aria from Rosanne, Lemarc
8 Tendi cuor from Il ritorno di Lisandro, Kreubel
9 Ove fuggono i dolci giorni, The Countess's aria from Il Ritorno di Lisandro - Kreubel
Nice to have
- We want a modern, attractive, perhaps provocative design. Be creative, please feel free to use any graphics from www.thearmonici-example.org, or www.wbfenwickopera-example.org

```html
<!DOCTYPE html>
<html lang="en">
<head>
<meta charset="utf-8">
<title>Hartwell Armonici Chamber Orchestra — Egle Marcinkute &amp; Tomas Brekvold</title>
<link rel="stylesheet" href="https://fonts.googleapis.com/css2?family=Cinzel:wght@400&family=Great+Vibes&family=Rye&family=Quicksand:wght@400&display=swap">
<style>
  :root {
    --bg: #151413;
    --bg-soft: #201f1d;
    --frame: #5c4d30;
    --title: #f2ead8;
    --script: #d6e8a2;
    --name: #7b7b78;
    --role: #a3a37f;
    --label-red: #e0100f;
    --flourish: #6e0d0d;
    --photo-light: #e6dc9c;
    --photo-mid: #7d8a5c;
    --photo-dark: #230f29;
  }
  * { margin: 0; padding: 0; box-sizing: border-box; }
  html, body { width: 1200px; height: 1200px; overflow: hidden; background: var(--bg); }
  .cover {
    position: relative; width: 1200px; height: 1200px; overflow: hidden;
    background: radial-gradient(ellipse at 50% 45%, var(--bg-soft) 0%, var(--bg) 75%);
  }
  .frame { position: absolute; inset: 0; }

  .flourish {
    position: absolute; left: 230px; top: 85px; width: 700px; height: 240px;
    background:
      radial-gradient(ellipse 38% 30% at 20% 25%, rgba(110,13,13,0.55) 0%, rgba(110,13,13,0) 100%),
      radial-gradient(ellipse 30% 40% at 85% 62%, rgba(110,13,13,0.6) 0%, rgba(110,13,13,0) 100%),
      radial-gradient(ellipse 45% 18% at 55% 58%, rgba(110,13,13,0.45) 0%, rgba(110,13,13,0) 100%);
  }

  .title {
    position: absolute; left: 0; width: 100%; text-align: center;
    font-family: "Cinzel", serif; font-weight: 400; color: var(--title);
    font-size: 78px; line-height: 1; letter-spacing: 2px;
  }
  .title--line1 { top: 118px; }
  .title--line2 { top: 200px; }
  .subtitle {
    position: absolute; top: 278px; left: 0; width: 100%; text-align: center;
    font-family: "Great Vibes", cursive; color: var(--script); font-size: 66px; line-height: 1;
  }

  .portrait {
    position: absolute; top: 348px; width: 415px; height: 603px;
    border: 1.5px solid var(--frame);
    border-radius: 208px 208px 0 0;
  }
  .portrait--soprano {
    left: 121px;
    background:
      radial-gradient(ellipse 38% 30% at 62% 40%, rgba(230,220,156,0.95) 0%, rgba(230,220,156,0) 100%),
      radial-gradient(ellipse 30% 22% at 25% 55%, rgba(230,220,156,0.7) 0%, rgba(230,220,156,0) 100%),
      radial-gradient(ellipse 60% 30% at 70% 90%, rgba(125,138,92,0.7) 0%, rgba(125,138,92,0) 100%),
      linear-gradient(170deg, var(--photo-mid) 0%, #3d3a35 45%, var(--photo-dark) 100%);
  }
  .portrait--conductor {
    left: 666px;
    background:
      radial-gradient(ellipse 34% 36% at 50% 45%, rgba(230,220,156,0.95) 0%, rgba(230,220,156,0) 100%),
      radial-gradient(ellipse 26% 16% at 72% 90%, rgba(230,220,156,0.75) 0%, rgba(230,220,156,0) 100%),
      linear-gradient(180deg, #2b1a2e 0%, var(--photo-dark) 100%);
  }

  .artist { position: absolute; top: 982px; width: 500px; text-align: center; }
  .artist--soprano { left: 78px; }
  .artist--conductor { left: 623px; }
  .artist__name { font-family: "Rye", serif; color: var(--name); font-size: 42px; line-height: 1.1; letter-spacing: 1px; }
  .artist__role { font-family: "Quicksand", sans-serif; color: var(--role); font-size: 36px; line-height: 1; margin-top: 20px; }

  .label {
    position: absolute; top: 93px; left: 951px; width: 140px; text-align: center;
    font-family: "Quicksand", sans-serif; color: var(--title); font-size: 11px;
  }
  .label__mark { display: block; width: 70px; height: 70px; margin: 0 auto 6px; background: var(--label-red); }
</style>
</head>
<body>
<main class="cover">
  <svg class="frame" width="1200" height="1200" viewBox="0 0 1200 1200" fill="none" stroke="#5c4d30" stroke-width="1.5">
    <g class="frame__half">
      <line x1="75" y1="0" x2="75" y2="1200"/>
      <line x1="1124" y1="0" x2="1124" y2="1200"/>
      <line x1="31" y1="71" x2="1169" y2="71"/>
      <polyline points="469,32 31,32 31,71"/>
      <polyline points="117,71 117,115 36,115 36,280"/>
      <polyline points="733,32 1169,32 1169,71"/>
      <polyline points="1086,71 1086,115 1167,115 1167,280"/>
    </g>
    <g class="frame__half" transform="translate(0,1200) scale(1,-1)">
      <line x1="31" y1="71" x2="1169" y2="71"/>
      <polyline points="469,32 31,32 31,71"/>
      <polyline points="117,71 117,115 36,115 36,280"/>
      <polyline points="733,32 1169,32 1169,71"/>
      <polyline points="1086,71 1086,115 1167,115 1167,280"/>
    </g>
  </svg>

  <div class="flourish" role="img" aria-label="Deep red calligraphic flourish ornament sweeping behind the title"></div>

  <div class="label"><span class="label__mark"></span>Armonici Records</div>

  <h1 class="title title--line1">HARTWELL</h1>
  <h1 class="title title--line2">ARMONICI</h1>
  <p class="subtitle">Chamber Orchestra</p>

  <div class="portrait portrait--soprano" role="img" aria-label="Duotone portrait photograph of soprano Egle Marcinkute, resting her chin on her hand"></div>
  <div class="portrait portrait--conductor" role="img" aria-label="Duotone portrait photograph of conductor Tomas Brekvold in a dark turtleneck"></div>

  <div class="artist artist--soprano">
    <p class="artist__name">Egle Marcinkute</p>
    <p class="artist__role">Soprano</p>
  </div>
  <div class="artist artist--conductor">
    <p class="artist__name">Tomas Brekvold</p>
    <p class="artist__role">Conductor</p>
  </div>
</main>
</body>
</html>
```